Business Card Design Project

Hello Designers, hope you are all aiming enjoy the weekend
I have the Business Logo (uploaded), you can alter the color which ever way you think would work,
Im looking for a simple yet striking feel, something which will stay memorable (I have uploaded 3 examples for you to flick through)
Information on the card, will just be the bare minimum,
Double Sided
Info being
i.e.
Name
Number
Website
ABN
Tobin Wexmoor
+468213579 (singapore)
+315792846 (Australia)
+729384615 (America)
www.lomevu-linkup.example
ABN 86420913
Enjoy,
Tobin
Industry/Entity Type
Business
Look and feel
Each slider illustrates characteristics of the customer's brand and the style your logo design should communicate.

```html
<!DOCTYPE html>
<html lang="en">
<head>
<meta charset="UTF-8">
<title>Lomevu Linkup — Business Card</title>
<link href="https://fonts.googleapis.com/css2?family=Didact+Gothic&display=swap" rel="stylesheet">
<style>
  :root {
    --page-bg: #ffffff;
    --card-black: #0b1012;
    --card-charcoal: #1a1e20;
    --band-teal: #0b3a40;
    --band-teal-light: #114a51;
    --brand-teal: #1a9cab;
    --text-light: #eef5f6;
    --card-radius: 12px;
  }
  html, body {
    margin: 0;
    padding: 0;
    width: 1200px;
    height: 1142px;
    overflow: hidden;
    background: var(--page-bg);
    font-family: "Didact Gothic", "Helvetica Neue", Arial, sans-serif;
  }
  .sheet {
    position: relative;
    width: 1200px;
    height: 1142px;
  }
  .card {
    position: absolute;
    left: 120px;
    width: 960px;
    height: 540px;
    border-radius: var(--card-radius);
    overflow: hidden;
    background: var(--card-black);
  }
  .card--front { top: 20px; }
  .card--back { top: 582px; }

  .pattern {
    position: absolute;
    left: 0;
    right: 0;
  }
  .pattern--front {
    top: 0;
    bottom: 0;
    background: radial-gradient(ellipse at 30% 40%, var(--card-charcoal) 0%, var(--card-black) 75%);
  }
  .pattern--dark-top {
    top: 0;
    height: 135px;
    background: linear-gradient(180deg, var(--card-charcoal), var(--card-black));
  }
  .pattern--teal-band {
    top: 135px;
    height: 272px;
    background: linear-gradient(180deg, var(--band-teal-light), var(--band-teal) 60%, #0a3136);
  }
  .pattern--dark-bottom {
    top: 407px;
    bottom: 0;
    background: linear-gradient(180deg, var(--card-charcoal), var(--card-black));
  }

  .brand__name {
    position: absolute;
    left: 88px;
    top: 62px;
    margin: 0;
    font-size: 82px;
    font-weight: 400;
    line-height: 1;
    color: var(--brand-teal);
    letter-spacing: 0.5px;
    white-space: nowrap;
  }
  .brand__mark {
    position: absolute;
    right: 16px;
    bottom: 18px;
    width: 108px;
    height: 108px;
    border-radius: 18px;
    background: var(--brand-teal);
  }

  .contact {
    position: absolute;
    left: 81px;
    top: 160px;
    color: var(--text-light);
  }
  .contact__name {
    margin: 0 0 24px;
    font-size: 31px;
    font-weight: 400;
    line-height: 1.2;
  }
  .contact__phones {
    margin: 0;
    padding: 0;
    list-style: none;
    font-size: 20px;
    line-height: 27px;
  }
  .business-info {
    position: absolute;
    right: 72px;
    top: 330px;
    text-align: right;
    color: var(--text-light);
    font-size: 20px;
    line-height: 27px;
  }
  .business-info p { margin: 0; }
</style>
</head>
<body>
<main class="sheet">
  <section class="card card--front" aria-label="Card front">
    <div class="pattern pattern--front" role="img" aria-label="Faint repeating brand emblem pattern in dark charcoal"></div>
    <h1 class="brand__name">Lomevu Linkup</h1>
    <span class="brand__mark" aria-hidden="true"></span>
  </section>

  <section class="card card--back" aria-label="Card back">
    <div class="pattern pattern--dark-top" role="img" aria-label="Faint repeating brand emblem pattern in dark charcoal"></div>
    <div class="pattern pattern--teal-band" role="img" aria-label="Faint repeating brand emblem pattern in deep teal"></div>
    <div class="pattern pattern--dark-bottom" role="img" aria-label="Faint repeating brand emblem pattern in dark charcoal"></div>

    <div class="contact">
      <h2 class="contact__name">Tobin Wexmoor</h2>
      <ul class="contact__phones">
        <li>+468213579 (singapore)</li>
        <li>+315792846 (Australia)</li>
        <li>+729384615 (America)</li>
      </ul>
    </div>
    <div class="business-info">
      <p class="business-info__web">www.lomevu-linkup.example</p>
      <p class="business-info__abn">ABN 86420913</p>
    </div>
  </section>
</main>
</body>
</html>
```